Halvorn Building Inc Business Card Design

We want a business card that stands out; we build high end commercial interiors so card should be professional yet creative and have an architectural/design feel , very clean lines

We have 6 employees so we must be able to change the name, cell and email on each person's card
For the proof Dale Pomfrey is the president
Office Number is (561) 482-3155, Cell ( 561 ) 823-4170

4700 Kestrel Lane Suite 215, Palm Beach Gardens, FL 33403
www.halvornbuild.example
CGC 047395 ( This license must legally be on card)

Target Market(s)

Asset Specialists , Developers, Building owners, architects, business owners

Industry/Entity Type

Construction Company

Contact Information for Business Card

We want a very high end clean look, must incorporate existing logo

Font styles to use
Other font styles liked:
• Gotham, trade gothic, Mrs. Eaves,modern 20, trim or designers' choice

Colors

Designer to choose colors to be used in the design.

Requirements
Must have
• Name, address, CGC 047395, www.halvornbuild.example
• 4700 Kestrel Lane Suite 215, Palm Beach Gardens, FL 33403
• each persons name, cell phone and individual email address ie dalep@halvornbuild.example

```html
<!DOCTYPE html>
<html lang="en">
<head>
<meta charset="utf-8">
<title>Halvorn Building Inc – Business Card</title>
<link rel="stylesheet" href="https://fonts.googleapis.com/css2?family=Montserrat:wght@400;500;700;800&display=swap">
<style>
  :root {
    --navy: #2e2a78;
    --green: #74b93c;
    --ink: #1f1c1a;
    --edge: #9a9a9a;
    --paper: #ffffff;
  }
  html, body {
    margin: 0;
    padding: 0;
    width: 1199px;
    height: 1200px;
    overflow: hidden;
    background: var(--paper);
    font-family: "Montserrat", Arial, sans-serif;
  }
  .card {
    position: absolute;
    left: 189px;
    width: 821px;
    height: 462px;
    border: 1px solid var(--edge);
    border-radius: 38px;
    background: var(--paper);
    overflow: hidden;
    box-sizing: border-box;
  }
  .card--front { top: 121px; }
  .card--back { top: 617px; }
  .card__bands {
    position: absolute;
    inset: 0;
    width: 100%;
    height: 100%;
  }
  .wordmark {
    position: absolute;
    color: var(--navy);
    font-weight: 800;
    line-height: 1;
  }
  .wordmark__name { display: block; letter-spacing: 0.02em; }
  .wordmark__sub { display: block; letter-spacing: 0.32em; }
  .wordmark--front { left: 52px; top: 300px; }
  .wordmark--front .wordmark__name { font-size: 80px; }
  .wordmark--front .wordmark__sub { font-size: 27px; margin-top: 12px; }
  .wordmark--back { left: 112px; top: 360px; }
  .wordmark--back .wordmark__name { font-size: 33px; }
  .wordmark--back .wordmark__sub { font-size: 11px; margin-top: 6px; }

  .contact {
    position: absolute;
    left: 381px;
    top: 66px;
    color: var(--ink);
  }
  .contact__name {
    margin: 0;
    font-size: 29px;
    font-weight: 700;
    letter-spacing: 0.01em;
  }
  .contact__title {
    margin: 2px 0 14px;
    font-size: 23px;
    font-weight: 400;
  }
  .contact__list { list-style: none; margin: 0; padding: 0; }
  .contact__item {
    display: flex;
    align-items: flex-start;
    font-size: 22px;
    line-height: 28px;
    letter-spacing: 0.02em;
    margin-bottom: 6px;
  }
  .contact__item--office { font-size: 25px; }
  .contact__icon {
    width: 26px;
    height: 28px;
    margin-right: 16px;
    flex: none;
    fill: var(--green);
  }
  .license {
    position: absolute;
    left: 381px;
    top: 396px;
    margin: 0;
    font-size: 18px;
    font-weight: 700;
    color: var(--navy);
    letter-spacing: 0.02em;
  }
</style>
</head>
<body>

<section class="card card--front" aria-label="Card front">
  <svg class="card__bands" viewBox="0 0 821 462" aria-hidden="true">
    <polygon points="678,139 739,139 821,295 821,411" fill="var(--navy)"/>
    <line x1="630" y1="110" x2="812" y2="450" stroke="var(--green)" stroke-width="16"/>
  </svg>
  <div class="wordmark wordmark--front">
    <span class="wordmark__name">HALVORN</span>
    <span class="wordmark__sub">BUILDING INC</span>
  </div>
</section>

<section class="card card--back" aria-label="Card back">
  <svg class="card__bands" viewBox="0 0 821 462" aria-hidden="true">
    <polygon points="87,139 150,139 0,415 0,303" fill="var(--navy)"/>
    <line x1="227" y1="45" x2="18" y2="440" stroke="var(--green)" stroke-width="16"/>
  </svg>
  <div class="wordmark wordmark--back">
    <span class="wordmark__name">HALVORN</span>
    <span class="wordmark__sub">BUILDING INC</span>
  </div>

  <div class="contact">
    <h1 class="contact__name">Dale Pomfrey</h1>
    <p class="contact__title">President</p>
    <ul class="contact__list">
      <li class="contact__item contact__item--office">
        <svg class="contact__icon" viewBox="0 0 26 28" aria-label="Office phone"><path d="M2 10c0-4 5-6 11-6s11 2 11 6v2h-6v-3H8v3H2z"/><path d="M5 14l3-4h10l3 4v8H5z"/><circle cx="13" cy="17" r="2.5" fill="#fff"/></svg>
        (561) 482-3155
      </li>
      <li class="contact__item">
        <svg class="contact__icon" viewBox="0 0 26 28" aria-label="Cell phone"><rect x="5" y="1" width="16" height="26" rx="3"/><rect x="8" y="4" width="10" height="16" fill="#fff"/><circle cx="13" cy="23.5" r="1.6" fill="#fff"/></svg>
        (561) 823-4170
      </li>
      <li class="contact__item">
        <svg class="contact__icon" viewBox="0 0 26 28" aria-label="Address"><path d="M13 1a9 9 0 0 1 9 9c0 7-9 17-9 17S4 17 4 10a9 9 0 0 1 9-9z"/><circle cx="13" cy="10" r="3.5" fill="#fff"/></svg>
        <span>4700 Kestrel Lane Suite 215,<br>Palm Beach Gardens, FL 33403</span>
      </li>
      <li class="contact__item">
        <svg class="contact__icon" viewBox="0 0 26 28" aria-label="Website"><circle cx="13" cy="14" r="10"/><g fill="none" stroke="#fff" stroke-width="1.6"><ellipse cx="13" cy="14" rx="4.5" ry="10"/><line x1="3" y1="14" x2="23" y2="14"/><line x1="5" y1="9" x2="21" y2="9"/><line x1="5" y1="19" x2="21" y2="19"/></g></svg>
        www.halvornbuild.example
      </li>
      <li class="contact__item">
        <svg class="contact__icon" viewBox="0 0 26 28" aria-label="Email"><rect x="2" y="6" width="22" height="16" rx="2"/><path d="M3 8l10 7 10-7" fill="none" stroke="#fff" stroke-width="1.8"/></svg>
        dalep@halvornbuild.example
      </li>
    </ul>
  </div>

  <p class="license">License# CGC 047395</p>
</section>

</body>
</html>
```